Professional
Miriam T. Hollisby, Esq.
Attorney at Law
Hollisby & Dunmore, LLC
4127 Fernhaven Court
Atlanta, Georgia 30305
mhollisby@hd-counsel.net
www.hd-counsel.net
I may want to include a photo. I have uploaded a photo. I'd like to see if it looks appropriate, if not, we'll go without a photo. Please use the logo that is uploaded
Please use the logo that is uploaded in some way. Possibly the corresponding black background with whitel letters for the back.
Photo to possibly be included on busines cards

```html
<!DOCTYPE html>
<html lang="en">
<head>
<meta charset="utf-8">
<title>Hollisby &amp; Dunmore, LLC — Business Cards</title>
<link rel="stylesheet" href="https://fonts.googleapis.com/css2?family=Cinzel:wght@400;600&display=swap">
<style>
  :root {
    --backdrop: #3a3a3c;
    --paper: #ffffff;
    --ink: #3b3b3b;
    --ink-soft: #6d6d6d;
    --red: #b3161b;
    --red-deep: #7d0b0f;
    --red-light: #d3272b;
    --black-card: #0c0c0c;
    --rule: #2a2a2a;
  }
  * { box-sizing: border-box; margin: 0; padding: 0; }
  html, body {
    width: 1200px; height: 754px; overflow: hidden;
    background: var(--backdrop);
    font-family: "Cinzel", "Times New Roman", serif;
  }
  .sheet { position: relative; width: 1200px; height: 754px; }

  .card {
    position: absolute; width: 500px; height: 290px;
    background: var(--paper);
    box-shadow: 0 8px 22px rgba(0,0,0,.45);
    overflow: hidden;
  }
  .card--front-a { left: 70px;  top: 70px; }
  .card--front-b { left: 630px; top: 70px; }
  .card--back-white { left: 70px;  top: 394px; }
  .card--back-black { left: 630px; top: 394px; background: var(--black-card); }

  /* brand lockup */
  .brand { display: flex; align-items: center; gap: 12px; }
  .brand__mark { width: 14px; height: 14px; background: var(--red); flex: none; }
  .brand__text { display: flex; flex-direction: column; }
  .brand__name { font-size: 19px; font-weight: 400; color: var(--ink); letter-spacing: .5px; white-space: nowrap; }
  .brand__tagline { font-size: 8px; font-weight: 600; color: var(--red); letter-spacing: 2.5px; text-transform: uppercase; margin-top: 2px; }
  .card--back-black .brand__name { color: #ffffff; }

  .red-band {
    position: absolute; left: 0; right: 0; bottom: 0;
    background: radial-gradient(ellipse at 50% 20%, var(--red-light) 0%, var(--red) 45%, var(--red-deep) 100%);
    border-top: 3px solid var(--rule);
    color: #fff;
  }

  .person__name { font-size: 14px; font-weight: 600; color: var(--ink); letter-spacing: .4px; }
  .person__title { font-size: 11px; color: var(--ink-soft); letter-spacing: .4px; margin-top: 3px; }

  .contact { font-size: 10px; line-height: 1.7; letter-spacing: .5px; color: #fff; }
  .contact--split { display: flex; align-items: center; }
  .contact__divider { width: 1px; height: 58px; background: rgba(255,255,255,.7); margin: 0 16px; }

  /* front A */
  .card--front-a .person { position: absolute; top: 24px; right: 26px; text-align: left; }
  .card--front-a .brand { position: absolute; top: 112px; left: 38px; }
  .card--front-a .red-band { height: 120px; }
  .card--front-a .contact--split { position: absolute; left: 120px; top: 28px; }

  /* front B */
  .card--front-b .brand { position: absolute; top: 40px; left: 36px; }
  .card--front-b .red-band { height: 168px; }
  .card--front-b .person { position: absolute; left: 36px; top: 62px; }
  .card--front-b .person__name,
  .card--front-b .person__title { color: #fff; }
  .card--front-b .contact { position: absolute; right: 36px; top: 20px; }

  /* backs */
  .card--back-white .brand,
  .card--back-black .brand { position: absolute; left: 50%; top: 120px; transform: translateX(-50%); }
  .web { position: absolute; left: 0; right: 0; bottom: 22px; text-align: center; font-size: 10px; color: var(--red); letter-spacing: .5px; }
</style>
</head>
<body>
<main class="sheet">

  <section class="card card--front-a">
    <div class="person">
      <p class="person__name">Miriam T. Hollisby, Esq.</p>
      <p class="person__title">Attorney at Law</p>
    </div>
    <div class="brand">
      <span class="brand__mark"></span>
      <div class="brand__text">
        <span class="brand__name">Hollisby &amp; Dunmore, LLC</span>
        <span class="brand__tagline">Attorneys at Law</span>
      </div>
    </div>
    <div class="red-band">
      <div class="contact contact--split">
        <address class="contact" style="font-style:normal">4127 Fernhaven Court<br>Atlanta, Georgia 30305</address>
        <span class="contact__divider"></span>
        <p class="contact">P : 404.555.0172<br>F : 404.555.0173<br>mhollisby@hd-counsel.net</p>
      </div>
    </div>
  </section>

  <section class="card card--front-b">
    <div class="brand">
      <span class="brand__mark"></span>
      <div class="brand__text">
        <span class="brand__name">Hollisby &amp; Dunmore, LLC</span>
        <span class="brand__tagline">Attorneys at Law</span>
      </div>
    </div>
    <div class="red-band">
      <div class="contact">
        4127 Fernhaven Court<br>Atlanta, Georgia 30305<br>P : 404.555.0172<br>F : 404.555.0173<br>mhollisby@hd-counsel.net<br>www.hd-counsel.net
      </div>
      <div class="person">
        <p class="person__name">Miriam T. Hollisby, Esq.</p>
        <p class="person__title">Attorney at Law</p>
      </div>
    </div>
  </section>

  <section class="card card--back-white">
    <div class="brand">
      <span class="brand__mark"></span>
      <div class="brand__text">
        <span class="brand__name">Hollisby &amp; Dunmore, LLC</span>
        <span class="brand__tagline">Attorneys at Law</span>
      </div>
    </div>
    <p class="web">www.hd-counsel.net</p>
  </section>

  <section class="card card--back-black">
    <div class="brand">
      <span class="brand__mark"></span>
      <div class="brand__text">
        <span class="brand__name">Hollisby &amp; Dunmore, LLC</span>
        <span class="brand__tagline">Attorneys at Law</span>
      </div>
    </div>
    <p class="web">www.hd-counsel.net</p>
  </section>

</main>
</body>
</html>
```